Hackthon event need a Landing Page

We are looking for a landing page to represent an event we are preparing in our country (Dominican Republic), it would be the first of this type, and we want to create a positive impact and make it a brand to make it recurring year to year .

The event is a hackathon where we will be gathering students and professionals to solve challenges using software development.

This landing page should be resposive, multi-language, clean, modern and align with the event logo.

Find a good example of what we are looking for in the following link:

https://brightcodefest.example/

We would like to have the following sections(Not necesarily in this order, not necesarily all of them):

- Brief
- Agenda
- Countdown
- Form Button to redirect to the event registration service.
---> Note: We would like to see the option of having the form in the landing page.
- Contact info and Social Media
- Partners/Sponsors
- Link to intro video

We will be attaching the logo and the variations of colors we are looking to see. It should be with a black background

```html
<!DOCTYPE html>
<html lang="en">
<head>
<meta charset="utf-8">
<title>BrightCode Hackathon</title>
<link href="https://fonts.googleapis.com/css2?family=Poppins:wght@400;500;600;700;800&display=swap" rel="stylesheet">
<style>
:root{
  --bg:#2b2b2b;
  --bg-dark:#1f1f21;
  --card:#2c2c2e;
  --teal:#14c8b5;
  --salmon:#e8735f;
  --text:#ffffff;
  --muted:#d9d9d9;
  --footer:#232323;
}
*{margin:0;padding:0;box-sizing:border-box}
html,body{width:1200px;height:4299px;overflow:hidden}
body{background:var(--bg);color:var(--text);font-family:"Poppins",sans-serif;position:relative}
section,header,footer{position:absolute;left:0;width:1200px}
.abs{position:absolute}
.center{left:0;width:1200px;text-align:center}
.title{font-weight:700;font-size:32px;letter-spacing:.5px;text-transform:uppercase}
.rule{position:absolute;left:555px;width:90px;height:3px;background:var(--salmon)}
.lead{font-size:14.5px;line-height:33px;color:var(--muted);text-align:center;left:160px;width:880px}
.lead.narrow{left:165px;width:870px}

/* hero */
.hero{top:0;height:746px;background:linear-gradient(135deg,#5a4a44 0%,#7a5a48 35%,#3d3b40 60%,#4a4750 100%)}
.hero-shade{position:absolute;inset:0;background:linear-gradient(180deg,rgba(0,0,0,.7) 0%,rgba(0,0,0,.25) 30%,rgba(0,0,0,.25) 70%,rgba(0,0,0,.4) 100%)}
.brand{left:75px;top:30px;display:flex;align-items:center;gap:10px}
.brand-dot{width:18px;height:18px;border-radius:50%;background:var(--teal)}
.brand-name{font-weight:700;font-size:24px;color:var(--text)}
.nav{top:94px;left:302px;display:flex;gap:32px;font-size:15.5px;font-weight:600}
.nav a{color:var(--text);text-decoration:none}
.btn-reg{left:961px;top:84px;width:165px;height:43px;background:var(--teal);color:#fff;font-weight:600;font-size:15.5px;display:flex;align-items:center;justify-content:center}
.hero-title{top:318px;font-weight:800;font-size:62px;letter-spacing:1px}
.hero-sub{top:398px;font-size:24px;line-height:36px;font-weight:500}

/* overview */
.overview{top:746px;height:481px;background:var(--bg)}
.btn{background:var(--teal);color:#fff;font-weight:600;font-size:17px;display:flex;align-items:center;justify-content:center}

/* agenda */
.agenda{top:1227px;height:960px;background:radial-gradient(ellipse at 60% 35%,#2a2c30 0%,#1c1c1e 70%)}
.day{position:absolute;width:327px;background:var(--card);padding:38px 0 0 18px}
.day h3{font-weight:400;font-size:20px;line-height:26px;padding-left:2px}
.day .date{color:var(--salmon);font-size:21px;line-height:26px;margin-bottom:10px}
.day li{list-style:none;font-size:14.5px;line-height:38.7px;white-space:nowrap}
.day li b{color:var(--teal);font-weight:500;margin-right:6px}

/* sponsors */
.sponsors{top:2187px;height:442px;background:var(--bg)}
.partner{font-size:34px;color:#c9c9c9;font-weight:600;white-space:nowrap}

/* video */
.video{top:2629px;height:876px;background:radial-gradient(ellipse at 50% 40%,#2a2a2c 0%,#1d1d1f 75%)}
.video-frame{left:164px;top:275px;width:872px;height:517px;background:linear-gradient(120deg,#5b4b45 0%,#3e3a3c 45%,#2c2f36 75%,#4a4346 100%)}

/* contact */
.contact{top:3505px;height:681px;background:var(--bg)}
.info{left:75px;display:flex;gap:14px;font-size:17px;line-height:27px;color:var(--text)}
.info svg{flex:0 0 26px;margin-top:2px}
.social{left:75px;top:551px;display:flex;gap:14px;font-size:14px;color:var(--salmon);font-weight:500}
.field{position:absolute;left:704px;width:423px;background:#fff;color:#555;font-size:15.5px;padding:0 14px;display:flex;align-items:center}
.submit{left:704px;top:522px;width:423px;height:59px;background:var(--teal);font-size:20px;font-weight:700;display:flex;align-items:center;justify-content:center}

footer{top:4186px;height:113px;background:var(--footer);text-align:center;font-size:16px;line-height:113px;color:#e5e5e5}
</style>
</head>
<body>

<header class="hero" role="img" aria-label="Photo of a team of young developers collaborating around computers in a brick-walled office">
  <div class="hero-shade"></div>
  <div class="abs brand"><span class="brand-dot"></span><span class="brand-name">BrightCode</span></div>
  <nav class="abs nav">
    <a href="#">HOME</a><a href="#">ABOUT US</a><a href="#">AGENDA</a><a href="#">SPONSORS</a><a href="#">CONTACT US</a><a href="#">/ EN ▾</a>
  </nav>
  <div class="abs btn-reg">REGISTRATION</div>
  <h1 class="abs center hero-title">BRIGHTCODE</h1>
  <p class="abs center hero-sub">The event is a hackathon where we will be gathering students and professionals<br>to solve challenges using software development.</p>
</header>

<section class="overview">
  <h2 class="abs center title" style="top:74px">Overview Company</h2>
  <div class="rule" style="top:136px"></div>
  <p class="abs lead narrow" style="top:172px">Sed ut perspiciatis unde omnis iste natus error sit voluptatem accusantium doloremque laudantium, totam rem<br>aperiam, eaque ipsa quae ab illo inventore veritatis et quasi architecto beatae vitae dicta sunt explicabo.<br>Nemo enim ipsam voluptatem quia voluptas sit aspernatur aut odit aut fugit, sed quia consequuntur magni<br>dolores eos qui ratione voluptatem sequi nesciunt..</p>
  <div class="abs btn" style="left:512px;top:337px;width:176px;height:49px">Learn More</div>
</section>

<section class="agenda">
  <h2 class="abs center title" style="top:80px">Agenda</h2>
  <div class="rule" style="top:141px"></div>
  <p class="abs lead narrow" style="top:175px">Sed ut perspiciatis unde omnis iste natus error sit voluptatem accusantium doloremque laudantium, totam rem<br>aperiam, eaque ipsa quae ab illo inventore veritatis et quasi architecto beatae.</p>

  <div class="day" style="left:75px;top:292px;height:384px">
    <h3>Day 1</h3><div class="date">25. 10. 2022</div>
    <ul><li><b>10:00- 13:00</b>Excepteur sint occaecat</li><li><b>10:00- 13:00</b>Cupidatat non proident</li><li><b>10:00- 13:00</b>Sunt in culpa qui officia</li><li><b>10:00- 13:00</b>Deserunt mollit anim</li><li><b>10:00- 13:00</b>Cupidatat non proident</li><li><b>10:00- 13:00</b>Sunt in culpa qui officia</li></ul>
  </div>
  <div class="day" style="left:437px;top:389px;height:384px">
    <h3>Day2</h3><div class="date">25. 10. 2022</div>
    <ul><li><b>10:00- 13:00</b>Excepteur sint occaecat</li><li><b>10:00- 13:00</b>Cupidatat non proident</li><li><b>10:00- 13:00</b>Sunt in culpa qui officia</li><li><b>10:00- 13:00</b>Deserunt mollit anim</li><li><b>10:00- 13:00</b>Cupidatat non proident</li><li><b>10:00- 13:00</b>Sunt in culpa qui officia</li></ul>
  </div>
  <div class="day" style="left:794px;top:485px;height:384px">
    <h3>Day3</h3><div class="date">25. 10. 2022</div>
    <ul><li><b>10:00- 13:00</b>Excepteur sint occaecat</li><li><b>10:00- 13:00</b>Cupidatat non proident</li><li><b>10:00- 13:00</b>Sunt in culpa qui officia</li><li><b>10:00- 13:00</b>Deserunt mollit anim</li><li><b>10:00- 13:00</b>Cupidatat non proident</li><li><b>10:00- 13:00</b>Sunt in culpa qui officia</li></ul>
  </div>
</section>

<section class="sponsors">
  <h2 class="abs center title" style="top:92px">Partners/Sponsors</h2>
  <div class="rule" style="top:153px"></div>
  <p class="abs lead narrow" style="top:186px">Sed ut perspiciatis unde omnis iste natus error sit voluptatem accusantium doloremque laudantium, totam rem<br>aperiam, eaque ipsa quae ab illo inventore veritatis et quasi architecto beatae.</p>
  <div class="abs partner" style="left:86px;top:303px">Veltrix</div>
  <div class="abs partner" style="left:296px;top:308px;font-size:28px">Marrow Agency</div>
  <div class="abs partner" style="left:545px;top:303px">Payvane</div>
  <div class="abs partner" style="left:770px;top:303px;font-weight:400">Lumen &amp; Lumen</div>
</section>

<section class="video">
  <h2 class="abs center title" style="top:78px">Introduction Video</h2>
  <div class="rule" style="top:138px"></div>
  <p class="abs lead narrow" style="top:171px">Sed ut perspiciatis unde omnis iste natus error sit voluptatem accusantium doloremque laudantium, totam rem<br>aperiam, eaque ipsa quae ab illo inventore veritatis et quasi architecto beatae.</p>
  <div class="abs video-frame" role="img" aria-label="Video still of developers reviewing code together at a workstation">
    <svg class="abs" style="left:392px;top:215px" width="88" height="88" viewBox="0 0 88 88">
      <circle cx="44" cy="44" r="40" fill="none" stroke="#fff" stroke-width="6"/>
      <path d="M34 26 L62 44 L34 62 Z" fill="#fff"/>
    </svg>
  </div>
</section>

<section class="contact">
  <h2 class="abs title" style="left:73px;top:72px">Contact Info</h2>
  <div class="abs" style="left:75px;top:136px;width:90px;height:3px;background:var(--salmon)"></div>
  <div class="abs brand" style="top:230px"><span class="brand-dot"></span><span class="brand-name">BrightCode</span></div>

  <div class="abs info" style="top:348px">
    <svg width="26" height="22" viewBox="0 0 26 22"><path d="M1 4 L8 1 L17 4 L25 1 V18 L17 21 L8 18 L1 21 Z" fill="var(--teal)"/><path d="M8 1 V18 M17 4 V21" stroke="var(--bg)" stroke-width="1.5"/></svg>
    <span>Nemo enim ipsam voluptatem<br>quia voluptas sit</span>
  </div>
  <div class="abs info" style="top:428px">
    <svg width="26" height="22" viewBox="0 0 26 22"><path d="M1 4 L8 1 L17 4 L25 1 V18 L17 21 L8 18 L1 21 Z" fill="var(--teal)"/><path d="M8 1 V18 M17 4 V21" stroke="var(--bg)" stroke-width="1.5"/></svg>
    <span>1-800-555-0148</span>
  </div>
  <div class="abs info" style="top:478px">
    <svg width="26" height="22" viewBox="0 0 26 22"><path d="M1 4 L8 1 L17 4 L25 1 V18 L17 21 L8 18 L1 21 Z" fill="var(--teal)"/><path d="M8 1 V18 M17 4 V21" stroke="var(--bg)" stroke-width="1.5"/></svg>
    <span>hello@brightcodefest.example</span>
  </div>
  <div class="abs social"><span>Friendly</span><span>Chirpy</span><span>Snapla</span><span>Linkup</span><span>Vidtube</span></div>

  <h2 class="abs title" style="left:702px;top:72px">Quick Registration</h2>
  <div class="abs" style="left:704px;top:136px;width:90px;height:3px;background:var(--salmon)"></div>
  <div class="field" style="top:175px;height:59px">Name</div>
  <div class="field" style="top:249px;height:57px">Email Address</div>
  <div class="field" style="top:322px;height:57px">Phone No</div>
  <div class="field" style="top:394px;height:115px;align-items:flex-start;padding-top:18px">Message</div>
  <div class="abs submit">SUBMIT</div>
</section>

<footer>Copyright© 2022 Company Name All Right Reserved</footer>

</body>
</html>
```